One of a Kind Clean Business Card

We need to design a new business card template for our company. Our company designs and produced merchandising displays. You can see a sample of what we produce on our site www.qorvatfixtures.com. I have uploaded our logo in vector format, as well as a picture of our current business cards. We want a totally different look. We want simple and clean, looking forward to seeing what people create.
Updates

I would like to update the address for Tellur Display Group Inc. 418 N Brindle Ave Arlington Heights, IL 60817 Would also note. No QR codes

Industry/Entity Type

Business

Contact Information for Business Card

Need a 1 sided business card designed.

Font styles to use
Serif

Requirements
Must have
• Easy to view; Clean Design
Nice to have
• Features that promote engineering and creativity
Should not have
• Too much clutter, keep it simple

```html
<!DOCTYPE html>
<html lang="en">
<head>
<meta charset="utf-8">
<title>Tellur Display Group Inc. – Business Card</title>
<link rel="stylesheet" href="https://fonts.googleapis.com/css2?family=Source+Serif+4:wght@400&display=swap">
<style>
  :root {
    --backdrop: #2b2b2b;
    --card: #111112;
    --card-panel: #1a1a1b;
    --ink-white: #f2f2f2;
    --ink-red: #b3242b;
  }
  * { box-sizing: border-box; margin: 0; padding: 0; }
  html, body { width: 1200px; height: 900px; overflow: hidden; }
  body {
    background: var(--backdrop);
    font-family: "Source Serif 4", Georgia, "Times New Roman", serif;
    display: flex;
    align-items: center;
    justify-content: center;
  }
  .card {
    position: relative;
    width: 900px;
    height: 520px;
    border-radius: 36px;
    background: var(--card);
    box-shadow: 0 14px 40px rgba(0,0,0,.45);
    overflow: hidden;
  }
  .brand-name {
    position: absolute;
    left: 66px;
    top: 262px;
    width: 360px;
    color: var(--ink-white);
    font-size: 34px;
    font-weight: 400;
    letter-spacing: .5px;
    text-transform: uppercase;
    line-height: 1.15;
  }
  .contact-panel {
    position: absolute;
    top: 0;
    right: 0;
    width: 430px;
    height: 100%;
    background: var(--card-panel);
    border-top-left-radius: 36px;
    border-bottom-left-radius: 36px;
    padding: 86px 0 0 50px;
    color: var(--ink-white);
  }
  .person-name {
    color: var(--ink-red);
    font-size: 30px;
    font-weight: 400;
    text-transform: uppercase;
    letter-spacing: .5px;
    margin-bottom: 22px;
  }
  .address { font-size: 21px; line-height: 1.4; margin-bottom: 20px; }
  .contact-list { list-style: none; font-size: 21px; line-height: 1.5; }
  .contact-list li { display: flex; align-items: center; gap: 14px; }
  .contact-list svg { width: 16px; height: 16px; flex: none; fill: var(--ink-red); }
</style>
</head>
<body>
  <section class="card" aria-label="Business card">
    <p class="brand-name">Tellur Display Group Inc.</p>
    <div class="contact-panel">
      <h1 class="person-name">Dana Ferrow</h1>
      <p class="address">418 N Brindle Ave<br>Arlington Heights, IL 60817</p>
      <ul class="contact-list">
        <li>
          <svg viewBox="0 0 12 12" aria-hidden="true"><path d="M2 1h2.5l1 3-1.5 1a6 6 0 0 0 3 3l1-1.5 3 1V11a1 1 0 0 1-1 1A10 10 0 0 1 1 2a1 1 0 0 1 1-1z"/></svg>
          815-555-0142
        </li>
        <li>
          <svg viewBox="0 0 12 12" aria-hidden="true"><path d="M3.5 0h5a1 1 0 0 1 1 1v10a1 1 0 0 1-1 1h-5a1 1 0 0 1-1-1V1a1 1 0 0 1 1-1zm.5 1.5v8h4v-8z"/></svg>
          312-555-0187
        </li>
        <li>
          <svg viewBox="0 0 12 12" aria-hidden="true"><path d="M0 2h12v1L6 7 0 3zm0 2.2 6 4 6-4V10H0z"/></svg>
          dferrow@qorvatfixtures.com
        </li>
        <li>
          <svg viewBox="0 0 12 12" aria-hidden="true"><circle cx="6" cy="6" r="6"/></svg>
          www.qorvatfixtures.com
        </li>
      </ul>
    </div>
  </section>
</body>
</html>
```